Business card design needed

A earthmoving company, in the background would be good if there could be a picture of a (scraper), we have a business card already with lumo stack you may be able to see that?

Industry/Entity Type

Business

Contact Information for Business Card

Company name: Brindle Earthmoving

Corwin Brindle
514 Tarrabin-Keswell Rd
Mount Jukes
4815
0491 736 052
corwin_brindle@mailbrook.net

on the rear of the card
Equipment Hire and Contract

All Earthmoving, Mining and Civil Contruction

```html
<!DOCTYPE html>
<html lang="en">
<head>
<meta charset="utf-8">
<title>Brindle Earthmoving — Business Card Rear</title>
<link rel="stylesheet" href="https://fonts.googleapis.com/css2?family=Arimo:wght@400;700&display=swap">
<style>
  :root {
    --card-yellow: #ebb220;
    --band-black: #0a0b0a;
    --ink: #0a0b0a;
    --mark-grey: #c3c5c4;
  }
  html, body {
    margin: 0;
    padding: 0;
    overflow: hidden;
    background: var(--card-yellow);
  }
  .card {
    position: relative;
    width: 1200px;
    height: 682px;
    background: var(--card-yellow);
    overflow: hidden;
    font-family: "Arimo", Arial, sans-serif;
  }
  .brand-band {
    position: absolute;
    left: 0;
    top: 92px;
    width: 1200px;
    height: 203px;
    background: var(--band-black);
  }
  .band-pointer {
    position: absolute;
    left: 150px;
    top: 294px;
    width: 44px;
    height: 39px;
  }
  .brand-name {
    position: absolute;
    left: 154px;
    top: 160px;
    margin: 0;
    font-size: 62px;
    font-weight: 700;
    line-height: 1;
    letter-spacing: -0.5px;
    color: var(--mark-grey);
  }
  .services {
    position: absolute;
    left: 88px;
    top: 378px;
    margin: 0;
    padding: 0;
    list-style: none;
  }
  .services li {
    position: relative;
    padding-left: 32px;
    font-size: 55px;
    font-weight: 400;
    line-height: 69px;
    color: var(--ink);
    white-space: nowrap;
  }
  .services li::before {
    content: "";
    position: absolute;
    left: 0;
    top: 29px;
    width: 14px;
    height: 14px;
    border-radius: 50%;
    background: var(--ink);
  }
</style>
</head>
<body>
  <main class="card">
    <div class="brand-band"></div>
    <svg class="band-pointer" viewBox="0 0 44 39" aria-hidden="true">
      <polygon points="0,0 44,0 21,39" fill="#0a0b0a"/>
    </svg>
    <p class="brand-name">Brindle Earthmoving</p>
    <ul class="services">
      <li>Equipment Hire and Contract</li>
      <li>All Earthmoving</li>
      <li>Mining and Civil Contruction</li>
    </ul>
  </main>
</body>
</html>
```